Brightstep Foot Care Advertisement Sandwich board

We need a Sandwich board design for our fungal nail clinic - please find attached the sandwich board dimensions.

The sandwich board itself will be displayed outside of a large health clinic and we need it to attract the attention of people walking by. We need a brochure holder included in the design which will hold our brochures which provides as clients with more information (please see attached also).

We are open to the designers creativity but we would like a similar theme portrayed on our board that is similar to our website (www.brightstepfootcare.co.nz) and brochure that incorporates our logo which I have attached). The final design should communicate professionalism and be a minimalist look but modern to capture the attention of pedestrians.

Finally, we would like the website and phone number (07) 312 5840.

We look forward to seeing your work.

```html
<!DOCTYPE html>
<html lang="en">
<head>
<meta charset="utf-8">
<title>Brightstep Foot Care – Sandwich Board</title>
<link href="https://fonts.googleapis.com/css2?family=Bebas+Neue&family=Cinzel:wght@400&family=Questrial&display=swap" rel="stylesheet">
<style>
  :root {
    --page-bg: #ececec;
    --brand-blue: #2f5aa8;
    --brand-blue-deep: #1b347f;
    --ink-dark: #14182c;
    --white: #ffffff;
    --slot: #6e6e6e;
  }
  html, body {
    margin: 0;
    padding: 0;
    width: 1200px;
    height: 2252px;
    overflow: hidden;
    background: var(--page-bg);
  }
  .board {
    position: absolute;
    left: 100px;
    top: 493px;
    width: 1000px;
    height: 1266px;
    background: var(--white);
    box-shadow: 0 10px 30px rgba(0,0,0,0.25);
    overflow: hidden;
  }
  .board-art {
    position: absolute;
    inset: 0;
  }
  .brand {
    position: absolute;
    left: 0;
    width: 505px;
    top: 60px;
    text-align: center;
    color: var(--white);
    font-family: "Cinzel", serif;
    font-weight: 400;
  }
  .brand-name {
    font-size: 48px;
    letter-spacing: 3px;
    line-height: 1;
    margin-top: 166px;
  }
  .brand-sub {
    font-size: 28px;
    letter-spacing: 10px;
    line-height: 1;
    margin-top: 18px;
  }
  .headline {
    position: absolute;
    left: 66px;
    top: 350px;
    width: 390px;
    margin: 0;
    font-family: "Bebas Neue", sans-serif;
    font-weight: 400;
    font-size: 108px;
    line-height: 104px;
    white-space: nowrap;
  }
  .headline span { display: block; }
  .headline .light { color: var(--white); }
  .headline .dark { color: var(--ink-dark); }
  .tagline {
    position: absolute;
    left: 68px;
    top: 708px;
    font-family: "Bebas Neue", sans-serif;
    font-size: 46px;
    color: var(--ink-dark);
    margin: 0;
  }
  .pill {
    position: absolute;
    background: var(--white);
    border-radius: 32px;
    font-family: "Bebas Neue", sans-serif;
    display: flex;
    align-items: center;
    white-space: nowrap;
  }
  .treatments-label {
    left: 67px;
    top: 803px;
    width: 343px;
    height: 62px;
    justify-content: center;
    color: var(--brand-blue);
    font-size: 42px;
  }
  .treatment-list {
    position: absolute;
    left: 80px;
    top: 880px;
    margin: 0;
    padding: 0;
    list-style: none;
    font-family: "Questrial", sans-serif;
    font-size: 35px;
    color: var(--white);
  }
  .treatment-list li {
    display: flex;
    align-items: center;
    height: 42px;
  }
  .treatment-list svg { margin-right: 14px; }
  .phone {
    left: 67px;
    top: 1140px;
    width: 316px;
    height: 62px;
    color: var(--ink-dark);
    font-size: 46px;
    gap: 12px;
    padding-left: 12px;
    box-sizing: border-box;
  }
  .web {
    left: 494px;
    top: 1143px;
    width: 438px;
    height: 59px;
    background: var(--brand-blue);
    color: var(--white);
    font-size: 35px;
    gap: 10px;
    padding-left: 10px;
    box-sizing: border-box;
  }
  .icon-dot {
    width: 44px;
    height: 44px;
    border-radius: 50%;
    display: flex;
    align-items: center;
    justify-content: center;
    flex: none;
  }
  .phone .icon-dot { background: var(--brand-blue); }
  .web .icon-dot { background: var(--white); width: 40px; height: 40px; }
</style>
</head>
<body>
  <main class="board">
    <svg class="board-art" viewBox="0 0 1000 1266" width="1000" height="1266">
      <defs>
        <linearGradient id="panelBlue" x1="0" y1="0" x2="0" y2="1">
          <stop offset="0" stop-color="#3361b0"/>
          <stop offset="1" stop-color="#1b347f"/>
        </linearGradient>
        <linearGradient id="legsTone" x1="0" y1="0" x2="1" y2="1">
          <stop offset="0" stop-color="#f6f4f1"/>
          <stop offset="0.45" stop-color="#edcdb6"/>
          <stop offset="1" stop-color="#f4f2ef"/>
        </linearGradient>
        <linearGradient id="clinicTone" x1="0" y1="0" x2="1" y2="1">
          <stop offset="0" stop-color="#c9a9b2"/>
          <stop offset="1" stop-color="#b23d8a"/>
        </linearGradient>
        <linearGradient id="toeTone" x1="0" y1="0" x2="1" y2="1">
          <stop offset="0" stop-color="#c7b79c"/>
          <stop offset="1" stop-color="#8f8a84"/>
        </linearGradient>
      </defs>

      <path class="photo-legs" role="img" aria-label="Photo of a woman's smooth bare legs and feet, one hand resting on the knee"
            d="M700 0 C600 150 520 300 530 440 C540 600 620 720 600 900 C585 1040 530 1180 430 1266 H1000 V0 Z"
            fill="url(#legsTone)"/>

      <path class="blue-panel" d="M652 0 C560 140 470 300 480 440 C490 600 580 720 560 900 C545 1040 470 1180 360 1266 H0 V0 Z"
            fill="url(#panelBlue)"/>
      <path class="accent-curve" d="M692 0 C592 150 506 300 516 440 C526 600 606 720 586 900 C572 1040 505 1180 395 1266"
            fill="none" stroke="var(--brand-blue)" stroke-width="7"/>

      <rect class="brochure-slot" x="421" y="67" width="180" height="45" rx="22" fill="var(--slot)"/>

      <circle class="brand-circle" cx="253" cy="129" r="66" fill="none" stroke="var(--white)" stroke-width="6"/>

      <circle class="photo-treatment" role="img" aria-label="Photo of cold laser treatment on a foot" cx="708" cy="985" r="118"
              fill="url(#clinicTone)" stroke="var(--brand-blue)" stroke-width="4"/>
      <circle class="photo-nail" role="img" aria-label="Close-up photo of a toenail being treated" cx="848" cy="1042" r="84"
              fill="url(#toeTone)" stroke="var(--brand-blue)" stroke-width="6"/>
    </svg>

    <div class="brand">
      <div class="brand-name">BRIGHTSTEP</div>
      <div class="brand-sub">FOOT CARE</div>
    </div>

    <h1 class="headline">
      <span class="light">BRIGHT</span>
      <span class="dark">STEP</span>
      <span class="light">FOOT CARE</span>
    </h1>

    <p class="tagline">YOUR FUNGAL NAIL EXPERT</p>

    <div class="pill treatments-label">TREATMENTS OFFERED</div>

    <ul class="treatment-list">
      <li><svg width="22" height="22" viewBox="0 0 22 22"><circle cx="11" cy="11" r="9" fill="none" stroke="#fff" stroke-width="2"/><path d="M6 11 l4 4 l7 -8" fill="none" stroke="#fff" stroke-width="2"/></svg>Cold Laser</li>
      <li><svg width="22" height="22" viewBox="0 0 22 22"><circle cx="11" cy="11" r="9" fill="none" stroke="#fff" stroke-width="2"/><path d="M6 11 l4 4 l7 -8" fill="none" stroke="#fff" stroke-width="2"/></svg>Topical</li>
      <li><svg width="22" height="22" viewBox="0 0 22 22"><circle cx="11" cy="11" r="9" fill="none" stroke="#fff" stroke-width="2"/><path d="M6 11 l4 4 l7 -8" fill="none" stroke="#fff" stroke-width="2"/></svg>Oral</li>
      <li><svg width="22" height="22" viewBox="0 0 22 22"><circle cx="11" cy="11" r="9" fill="none" stroke="#fff" stroke-width="2"/><path d="M6 11 l4 4 l7 -8" fill="none" stroke="#fff" stroke-width="2"/></svg>Surgery</li>
      <li><svg width="22" height="22" viewBox="0 0 22 22"><circle cx="11" cy="11" r="9" fill="none" stroke="#fff" stroke-width="2"/><path d="M6 11 l4 4 l7 -8" fill="none" stroke="#fff" stroke-width="2"/></svg>General Nail Care</li>
    </ul>

    <div class="pill phone">
      <span class="icon-dot">
        <svg width="24" height="24" viewBox="0 0 24 24"><path d="M6.6 10.8a15 15 0 0 0 6.6 6.6l2.2-2.2a1 1 0 0 1 1-.25 11.4 11.4 0 0 0 3.6.57 1 1 0 0 1 1 1V20a1 1 0 0 1-1 1A17 17 0 0 1 3 4a1 1 0 0 1 1-1h3.5a1 1 0 0 1 1 1c0 1.25.2 2.45.57 3.57a1 1 0 0 1-.25 1z" fill="#fff"/></svg>
      </span>
      (07) 312 5840
    </div>

    <div class="pill web">
      <span class="icon-dot">
        <svg width="26" height="26" viewBox="0 0 24 24"><circle cx="12" cy="12" r="9" fill="none" stroke="#2f5aa8" stroke-width="2"/><path d="M3 12h18M12 3c3 3 3 15 0 18M12 3c-3 3-3 15 0 18" fill="none" stroke="#2f5aa8" stroke-width="1.6"/></svg>
      </span>
      WWW.BRIGHTSTEPFOOTCARE.CO.NZ
    </div>
  </main>
</body>
</html>
```